Business Card Re-Design for a Lighting Designer

I would like my business card re-designed. It is currently high gloss and they scratch too easily. I don not think the current design lends itself well to a matte finish. I have included the current design for reference along with our company logo.
Check out our website for current branding.
http://www.brambleorchidstudio.example

Updates
Some of the top contenders are muslim and it is a holiday for them. I do not want to discriminate and would expect the same courtesy for holidays we celebrate.
Target Market(s)
Interior Designers, Architects
Contact Information for Business Card
Logo - Name, Title, Address, Telephone Number and Extension, Email
Font styles to use
Requirements
Must have
- All the information listed on the current business card. If you use Red, it needs to be the red from our logo.
Nice to have
- Vertical and Horizontal Designs will be entertained.
Should not have
- Requirements for a glossy finish...should not look too corporate since we are a design firm.

```html
<!DOCTYPE html>
<html lang="en">
<head>
<meta charset="utf-8">
<title>Bramble Orchid Studio – Business Card</title>
<link href="https://fonts.googleapis.com/css2?family=Roboto:wght@400;500&family=Questrial&display=swap" rel="stylesheet">
<style>
  :root {
    --page-bg: #d8d2ca;
    --card-top: #f2f1ee;
    --card-bottom: #e2dfda;
    --brand-red: #6b181c;
    --band-dark: #5a1216;
    --band-light: #7c2428;
    --ink: #1d1d1d;
    --ink-muted: #6a6866;
    --band-text: #e9d9d9;
    --edge: #a9a6a2;
  }
  * { box-sizing: border-box; margin: 0; padding: 0; }
  html, body { width: 1200px; height: 970px; overflow: hidden; }
  body { background: var(--page-bg); position: relative; }

  .card {
    position: absolute; left: 80px; top: 190px;
    width: 1040px; height: 592px;
    background: linear-gradient(180deg, var(--card-top), var(--card-bottom));
    box-shadow: 0 18px 40px rgba(0,0,0,.18);
    overflow: hidden;
  }

  .brand {
    position: absolute; right: 60px; top: 64px;
    display: flex; flex-direction: column; align-items: flex-end;
    font-family: "Roboto", sans-serif; font-weight: 400;
    color: var(--ink);
  }
  .brand-square { width: 168px; height: 168px; background: var(--brand-red); margin-bottom: 22px; }
  .brand-name { font-size: 46px; line-height: 1.02; text-align: right; letter-spacing: -0.5px; }

  .holder { position: absolute; left: 60px; top: 322px; font-family: "Roboto", sans-serif; }
  .holder-name { font-size: 38px; font-weight: 400; color: var(--ink); letter-spacing: 0; line-height: 1; }
  .holder-title {
    display: flex; align-items: center; gap: 16px; margin-top: 8px;
    font-size: 20px; font-weight: 500; letter-spacing: 5px; color: var(--ink-muted);
  }
  .holder-title::after { content: ""; width: 126px; height: 2px; background: var(--ink-muted); }

  .contact-band {
    position: absolute; left: 0; top: 426px; width: 100%; height: 146px;
    background: linear-gradient(90deg, var(--band-dark), var(--band-light) 45%, var(--band-dark));
    font-family: "Questrial", sans-serif; font-size: 23px; color: var(--band-text);
  }
  .card-edge { position: absolute; left: 0; bottom: 0; width: 100%; height: 20px; background: linear-gradient(180deg, #c9c6c2, var(--edge)); }

  .contact-list { position: absolute; left: 62px; top: 24px; list-style: none; }
  .contact-list li { display: flex; align-items: center; gap: 18px; height: 31px; letter-spacing: .5px; }
  .contact-list svg { width: 20px; height: 20px; fill: none; stroke: var(--band-text); stroke-width: 1.6; }

  .address { position: absolute; right: 60px; top: 24px; text-align: right; font-style: normal; line-height: 31px; letter-spacing: .5px; }
</style>
</head>
<body>
  <div class="card">
    <div class="brand">
      <div class="brand-square"></div>
      <div class="brand-name">BRAMBLE ORCHID<br>STUDIO</div>
    </div>

    <div class="holder">
      <p class="holder-name">MAREN HOLLOWAY</p>
      <p class="holder-title">PRINCIPAL</p>
    </div>

    <div class="contact-band">
      <ul class="contact-list">
        <li>
          <svg viewBox="0 0 20 20" aria-hidden="true"><rect x="5" y="2" width="10" height="16" rx="1.5"/><line x1="9" y1="15" x2="11" y2="15"/></svg>
          555.014.2280 x1
        </li>
        <li>
          <svg viewBox="0 0 20 20" aria-hidden="true"><rect x="2" y="5" width="16" height="11"/><polyline points="2,5 10,11 18,5"/></svg>
          maren@brambleorchidstudio.example
        </li>
        <li>
          <svg viewBox="0 0 20 20" aria-hidden="true"><circle cx="10" cy="10" r="7.5"/><ellipse cx="10" cy="10" rx="3.5" ry="7.5"/><line x1="2.5" y1="10" x2="17.5" y2="10"/></svg>
          www.brambleorchidstudio.example
        </li>
      </ul>
      <address class="address">
        418 Larkspur Mill Road<br>
        Suite 210 Fairhaven<br>
        Oregon 97000 USA
      </address>
    </div>
    <div class="card-edge"></div>
  </div>
</body>
</html>
```